Branding product image: TOMBEL (Golden Papaya) in Plastic Cup (Ready to Eat)

The product is sliced Fruit in Light syrup
Flavour: TOMBEL (Golden Papaya)
The temporary product name: TOMBEL
I want the product design to be something 'fun', 'natural', and 'colourful'
The design concept could be anything depends on your imagination, but it must be eye catchy and attractive.
Basically, I want you to be creative in designing the logo and the overall graphic design for the label.
The measurement is 20 cm (Length) x 6,5 cm (Height)
The target customers are young and health conscious audiences (10 years - 65 years old).
Create something different. Something extraordinary.
Brief summary about the fruit:
This fruit only grows in certain part of the world. It grows in mountain area that is in tropical climate. The fruit flesh has a yellowish-golden color. It has an extraordinary taste (unlike normal papaya) and it suits very well with any dishes from cold appetizer, white/ red meat, desserts, and cocktails.
I need a packaging design for Fruit Cup productThe product is sliced Fruit in Light syrup.There will be various flavours i.e. apple, lychee, peach, papaya, etc.However, you may design the product using one sample flavour (i.e. papaya) first, as the designs of other flavours could be adjusted afterwards.The temporary product name is: RICCANAI want the product design to be something 'fun', 'natural', and 'colourful'.The design concept could be anything depends on your imagination. Basically, I want you to be creative in designing the logo and the overall graphic design for the label. - Create something different. Something extraordinary -Additional:The measurement is 20cm (Length) x 5cm (Height).The target customers are young audiences (10 years - 35 years old).The product design must stand out in the supermarket shelf.It must be eye catchy and attractive.Thank you,Harold-PLEASE REFER TO DESIGN SAMPLE ATTACHED TO HAVE A BETTER UNDERSTANDING FOR THE PRODUCT CONCEPT- Added Wednesday, September 17, 2014
Project Deadline Extended Reason: Haven't found a good design. Added Friday, September 19, 2014
Project Deadline Extended Reason: Need more time for designers to finalize and perfect the design.Thank you,Harold Added Monday, September 29, 2014
Project Deadline Extended Reason: I haven't found a great design yet. Added Tuesday, February 24, 2015
Reason: Getting better designs now. Still Open to new ideas while refining the latest designs from some designers.
Please do your best in submitting other great designs!

```html
<!DOCTYPE html>
<html lang="en">
<head>
<meta charset="utf-8">
<title>Lupedos Lychee – Fruit Cup Label</title>
<link rel="stylesheet" href="https://fonts.googleapis.com/css2?family=Chewy&family=Lora:ital@0;1&display=swap">
<style>
  :root {
    --page: #ffffff;
    --sky-top: #ffffff;
    --aqua: #3ff2dc;
    --aqua-soft: #b9f4f0;
    --frame: #31d8ee;
    --sun: #fbb12a;
    --lime: #46f516;
    --crimson: #c40b1a;
    --blush: #f2c6c8;
    --pink: #f77fd3;
    --grass: #1e7d2c;
    --orange: #fb7d0c;
    --slogan: #1f5f2a;
    --info-ink: #222222;
  }
  html, body {
    margin: 0;
    width: 1200px;
    height: 422px;
    overflow: hidden;
    background: var(--page);
  }
  .label { display: block; width: 1200px; height: 422px; }
  .flavour {
    font-family: "Chewy", cursive;
    font-size: 31px;
    fill: var(--crimson);
    stroke: #f7e36b;
    stroke-width: 1.4px;
    paint-order: stroke;
  }
  .brand-name {
    font-family: "Lora", serif;
    font-size: 26px;
    fill: var(--crimson);
  }
  .slogan {
    font-family: "Lora", serif;
    font-style: italic;
    font-size: 15.5px;
    fill: var(--slogan);
  }
  .info-text {
    font-family: Arial, Helvetica, sans-serif;
    font-size: 8.6px;
    fill: var(--info-ink);
  }
</style>
</head>
<body>
<svg class="label" viewBox="0 0 1000 351.667" xmlns="http://www.w3.org/2000/svg">
  <defs>
    <linearGradient id="sky" x1="0" y1="0" x2="0" y2="1">
      <stop offset="0" stop-color="var(--sky-top)"/>
      <stop offset="0.3" stop-color="var(--aqua-soft)"/>
      <stop offset="0.55" stop-color="var(--aqua)"/>
    </linearGradient>
    <radialGradient id="sunGlow">
      <stop offset="0.7" stop-color="var(--sun)"/>
      <stop offset="1" stop-color="#fff6c8" stop-opacity="0"/>
    </radialGradient>
    <linearGradient id="palmTone" x1="0" y1="0" x2="1" y2="1">
      <stop offset="0" stop-color="#2fbf2a"/>
      <stop offset="0.7" stop-color="#1fd12e"/>
      <stop offset="1" stop-color="#b3272b"/>
    </linearGradient>
    <radialGradient id="pinkBloom">
      <stop offset="0" stop-color="#c9fff2"/>
      <stop offset="0.35" stop-color="#f59be0"/>
      <stop offset="1" stop-color="#f77fd3" stop-opacity="0.85"/>
    </radialGradient>
    <radialGradient id="yellowBloom">
      <stop offset="0" stop-color="#bff7d8"/>
      <stop offset="0.4" stop-color="#ffd814"/>
      <stop offset="1" stop-color="#ffe246" stop-opacity="0.8"/>
    </radialGradient>
    <radialGradient id="greenBloom">
      <stop offset="0" stop-color="#ffffff"/>
      <stop offset="0.5" stop-color="#bff5c3"/>
      <stop offset="1" stop-color="#6fe86d" stop-opacity="0.85"/>
    </radialGradient>
    <clipPath id="labelArea"><rect x="56" y="49" width="874" height="220"/></clipPath>
  </defs>

  <g class="label-art" clip-path="url(#labelArea)">
    <rect class="sky" x="56" y="49" width="874" height="220" fill="url(#sky)"/>
    <circle class="sun" cx="488" cy="100" r="50" fill="url(#sunGlow)"/>

    <rect class="band-lime" x="130" y="87" width="480" height="60" rx="24" fill="var(--lime)"/>
    <rect class="band-crimson" x="225" y="97" width="760" height="52" rx="26" fill="var(--crimson)"/>
    <rect class="band-aqua" x="56" y="148" width="874" height="24" fill="var(--aqua)"/>
    <rect class="flavour-tab" x="378" y="128" width="210" height="60" rx="26" fill="var(--pink)"/>

    <rect class="field-blush" x="110" y="168" width="680" height="80" rx="30" fill="var(--blush)"/>
    <rect class="field-blush" x="56" y="172" width="140" height="76" fill="var(--blush)"/>
    <rect class="strip-orange" x="56" y="198" width="13" height="71" fill="var(--orange)"/>
    <rect class="band-aqua-low" x="69" y="245" width="861" height="24" fill="var(--aqua)"/>

    <rect class="bar-lime" x="120" y="225" width="522" height="18" rx="9" fill="var(--lime)"/>
    <rect class="bar-grass" x="120" y="236" width="238" height="6" rx="3" fill="var(--grass)"/>
    <rect class="bar-grass" x="765" y="238" width="170" height="5" fill="var(--grass)"/>

    <g class="bubbles" fill="#ffffff" fill-opacity="0.45">
      <circle cx="542" cy="113" r="12"/>
      <circle cx="583" cy="134" r="22"/>
      <circle cx="636" cy="163" r="28"/>
      <circle cx="555" cy="172" r="9"/>
    </g>

    <rect class="palm-illustration" x="62" y="55" width="185" height="188" rx="60"
          fill="url(#palmTone)" role="img" aria-label="Palm tree illustration leaning over the beach"/>

    <circle class="bloom-pink" cx="705" cy="222" r="55" fill="url(#pinkBloom)"
            role="img" aria-label="Pink tropical blossom cluster"/>
    <circle class="bloom-green" cx="806" cy="200" r="46" fill="url(#greenBloom)"
            role="img" aria-label="Pale green bubble blossom"/>
    <circle class="bloom-yellow" cx="788" cy="135" r="45" fill="url(#yellowBloom)"
            role="img" aria-label="Yellow tropical blossom cluster"/>

    <text class="flavour" x="490" y="160" text-anchor="middle">Lychee</text>

    <g class="brand">
      <circle cx="436" cy="205" r="7" fill="var(--pink)"/>
      <text class="brand-name" x="498" y="214" text-anchor="middle">Lupedos</text>
    </g>

    <text class="slogan" x="490" y="261" text-anchor="middle">Slogan Lupedos fruit in light syrup</text>
  </g>

  <rect class="label-frame" x="56" y="49" width="874" height="220" fill="none" stroke="var(--frame)" stroke-width="1"/>

  <g class="info-panel">
    <rect x="851" y="63" width="70" height="196" fill="#ffffff" stroke="var(--frame)" stroke-width="1"/>
    <g transform="translate(886 161) rotate(-90)">
      <text class="info-text" x="0" y="-7" text-anchor="middle">ingredients and product information</text>
      <text class="info-text" x="0" y="3" text-anchor="middle">ingredients and product information</text>
      <text class="info-text" x="0" y="13" text-anchor="middle">ingredients and product information</text>
    </g>
  </g>
</svg>
</body>
</html>
```